Re-design and craft the perfect CV platform

We are building a CV-based platform designed to connect employees and employers, with a strong focus on individual users. As we're just starting out, we're looking to have our platform and logo redesigned to better reflect our vision
https://app.lumoshire.com/
Colors like in the logo attached
#87C032 #6A6E71 #618930 - also you can add more colors if you like.
https://app.lumoshire.com/dashboard - This page would be nice if you plan it, like personal Bio dashboard. Attached picture (Dashboard wanted) one idea from how we would like to be, but we are open for new professional ideas/solutions.
https://app.lumoshire.com/posts - On this page we want to be showed the jobs posted. Attached one picture about our idea (jobs page wanted)
https://app.lumoshire.com/profile - design something nice.
Only Photoshop, Illustrator or Figma
Other pictures from the app attached (as looking right now)

Target Market(s)

Job seekers, HR, Recruiters

Industry/Entity Type

HR Tech

Number of Pages Required

5+ page

Colors
00AB8E
00BBA5
67D7C9
C6EFE9
E9F9F6

```html
<!DOCTYPE html>
<html lang="en">
<head>
<meta charset="utf-8">
<title>Lumoshire – Recruitment, Training, Development</title>
<link rel="stylesheet" href="https://fonts.googleapis.com/css2?family=Poppins:wght@400;500;600;700;800&family=Montserrat:wght@500;600;700&display=swap">
<style>
:root{
  --green:#87C032;
  --green-dark:#618930;
  --grey:#6A6E71;
  --ink:#1b1b1b;
  --text:#333;
  --pale:#E6EBE0;
  --footer:#121212;
  --white:#fff;
}
*{box-sizing:border-box;margin:0;padding:0}
html,body{width:1200px;height:3874px;overflow:hidden}
body{font-family:"Poppins",sans-serif;color:var(--text);background:var(--white);position:relative}
section,header,footer{position:absolute;left:0;width:1200px;overflow:hidden}
.btn{display:inline-flex;align-items:center;justify-content:center;border-radius:30px;font-weight:500;font-size:15px;text-transform:uppercase;background:var(--green);color:#1b2a0a;position:absolute}
.accent{color:var(--green)}
.section-title{font-family:"Poppins",sans-serif;font-weight:700;font-size:34px;color:var(--grey);position:absolute;letter-spacing:.5px}

/* Header */
.site-header{top:0;height:108px;background:var(--white)}
.brand{position:absolute;left:112px;top:30px;display:flex;align-items:center;gap:10px}
.brand-mark{width:24px;height:24px;background:var(--green)}
.brand-name{font-weight:700;font-size:26px;color:var(--green);letter-spacing:.5px}
.main-nav{position:absolute;left:352px;top:56px;display:flex;font-size:14px;color:#333}
.main-nav a{color:inherit;text-decoration:none;margin-right:30px}
.main-nav a.active{color:var(--green);text-decoration:underline}
.login{left:974px;top:48px;width:114px;height:36px;font-size:14px}

/* Hero */
.hero{top:108px;height:519px}
.hero-photo{position:absolute;inset:0;background:linear-gradient(120deg,#2c3e4f 0%,#4a5a68 35%,#6b6f72 55%,#3d4650 80%,#22303c 100%)}
.hero-shade{position:absolute;inset:0;background:rgba(0,0,0,.25)}
.hero h1{position:absolute;top:146px;width:100%;text-align:center;color:#fff;font-weight:700;font-size:42px}
.hero-tags{position:absolute;top:218px;width:100%;display:flex;justify-content:center;gap:32px;color:#fff;font-size:17px;font-weight:500}
.hero-tags span::before{content:"";display:inline-block;width:8px;height:8px;border-radius:50%;background:#fff;margin-right:4px;vertical-align:middle}
.search{position:absolute;left:319px;top:284px;width:562px;height:52px;background:#fff;border-radius:30px;display:flex;align-items:center;font-size:16px;color:#333;padding-left:38px}
.search .sep{margin:0 24px;color:#666}
.caret{display:inline-block;border:5px solid transparent;border-top:6px solid #333;margin-left:6px;vertical-align:-3px}
.search-btn{position:absolute;right:4px;top:4px;width:46px;height:44px;border-radius:50%;background:var(--green)}

/* Services */
.services{top:627px;height:666px}
.services .section-title{left:111px;top:60px}
.service-card{position:absolute;top:143px;width:310px;height:430px;background:var(--grey);color:#fff;text-align:center}
.service-card.featured{background:var(--green)}
.service-photo{position:absolute;left:6px;top:6px;width:298px;height:184px}
.service-card h3{position:absolute;top:218px;width:100%;font-size:20px;font-weight:600}
.service-card p{position:absolute;top:250px;left:20px;right:20px;font-size:13px;line-height:23px}
.service-card .btn{top:358px;left:91px;width:130px;height:33px;font-size:14px}
.service-card.featured .btn{background:transparent;border:2px solid #1b2a0a}

/* About */
.about{top:1293px;height:438px;background:var(--pale)}
.about-mark{position:absolute;left:111px;top:113px;width:420px;height:226px;display:flex;align-items:center;justify-content:center;gap:14px}
.about-mark .mark{width:60px;height:60px;background:var(--green)}
.about-mark .name{font-weight:700;font-size:56px;color:var(--green)}
.about .section-title{left:610px;top:66px;color:var(--ink)}
.about p{position:absolute;left:610px;top:124px;width:465px;font-size:14px;line-height:27.5px;color:#333}
.about .btn{left:610px;top:361px;width:131px;height:35px;font-size:14px}

/* Mission */
.mission{top:1731px;height:507px;background:var(--green)}
.mission-photo{position:absolute;inset:0;background:linear-gradient(90deg,rgba(97,137,48,.35),rgba(135,192,50,.1) 50%,rgba(97,137,48,.35))}
.mission h2{position:absolute;top:66px;width:100%;text-align:center;font-size:35px;font-weight:600;color:var(--ink);letter-spacing:1px}
.mission p{position:absolute;left:165px;width:870px;text-align:center;font-size:17.5px;line-height:32px;color:#222}
.mission .p1{top:124px}
.mission .p2{top:222px}
.mission .btn{left:514px;top:380px;width:172px;height:52px;background:#fff;text-transform:none;font-size:15px;color:#222}

/* What we do */
.what{top:2238px;height:450px}
.what .section-title{left:111px;top:80px;color:var(--ink)}
.what p{position:absolute;left:112px;top:136px;width:428px;font-size:14px;line-height:25.8px;color:#333}
.what .btn{left:112px;top:326px;width:131px;height:34px;font-size:14px}
.monitor{position:absolute;left:650px;top:55px;width:382px;height:331px;border-radius:10px;background:linear-gradient(160deg,#f1f3ee,#d9ddd6)}

/* News */
.news{top:2688px;height:810px}
.news h2{position:absolute;top:28px;width:100%;text-align:center;font-size:35px;font-weight:600;color:var(--ink);letter-spacing:.5px}
.news-card{position:absolute;background:#fff;border-radius:18px;box-shadow:0 4px 22px rgba(0,0,0,.08);text-align:center}
.news-photo{position:absolute;left:128px;top:111px;width:275px;height:236px;border-radius:22px}
.news-card h3{font-size:21.5px;font-weight:500;line-height:30px;color:var(--ink)}
.news-card p{font-size:14px;line-height:26px;color:#333}
.learn{font-size:15px;font-weight:500;color:var(--green);display:inline-flex;align-items:center;gap:2px}
.tall{top:229px;width:310px;height:403px;padding:146px 20px 0}
.tall h3{margin-bottom:16px}
.tall p{margin-bottom:12px}
.short{left:777px;width:310px;height:256px;padding:22px 18px 0}
.short h3{margin-bottom:6px}
.short p{margin-bottom:10px}
.news .btn{left:524px;top:705px;width:152px;height:52px;font-size:15px}

/* Footer */
.site-footer{top:3498px;height:376px;background:var(--footer);color:#fff}
.footer-rings{position:absolute;left:-120px;top:-40px}
.footer-brand{position:absolute;left:128px;top:110px;display:flex;align-items:center;gap:12px}
.footer-brand .mark{width:34px;height:34px;background:var(--green)}
.footer-brand .name{font-weight:700;font-size:42px;color:var(--green)}
.site-footer h4{position:absolute;top:70px;font-size:21px;font-weight:600;letter-spacing:.3px}
.contact h4{left:454px}
.contact-list{position:absolute;left:454px;top:116px;font-size:14px;line-height:23px;list-style:none}
.contact-list li{display:flex;gap:10px;margin-bottom:12px}
.contact-list svg{flex:none;margin-top:4px}
.newsletter h4{left:717px}
.subscribe{position:absolute;left:717px;top:123px;width:336px;height:34px;background:#fff;border-radius:20px;font-size:14px;color:#333;padding:8px 18px}
.subscribe .btn{right:0;top:0;height:34px;width:120px;text-transform:none;font-size:14px;color:#1b2a0a}
.legal{position:absolute;top:332px;font-size:13px}
.legal.left{left:108px}
.legal.right{right:112px}
</style>
</head>
<body>

<header class="site-header">
  <div class="brand"><span class="brand-mark"></span><span class="brand-name">LUMOSHIRE</span></div>
  <nav class="main-nav">
    <a class="active" href="#">Home</a><a href="#">About Us</a><a href="#">Recruitment</a><a href="#">Job Seekers</a><a href="#">Industry</a><a href="#">News</a><a href="#">Contact Us</a>
  </nav>
  <a class="btn login" href="#">LOGIN</a>
</header>

<section class="hero">
  <div class="hero-photo" role="img" aria-label="Photo of two businessmen shaking hands in an office"></div>
  <div class="hero-shade"></div>
  <h1>WELCOME TO LUMOSHIRE</h1>
  <div class="hero-tags"><span>Recruitment</span><span>Training</span><span>Development</span></div>
  <div class="search">
    <span>Search jobs</span><span class="sep">|</span><span>Country<i class="caret"></i></span><span class="sep">|</span><span>Category<i class="caret"></i></span>
    <span class="search-btn">
      <svg width="46" height="44" viewBox="0 0 46 44"><circle cx="22" cy="21" r="5" fill="none" stroke="#1b2a0a" stroke-width="2.4"/><line x1="25.5" y1="24.5" x2="29" y2="28" stroke="#1b2a0a" stroke-width="2.6" stroke-linecap="round"/></svg>
    </span>
  </div>
</section>

<section class="services">
  <h2 class="section-title"><span class="accent">OUR</span> SERVICES</h2>
  <article class="service-card" style="left:111px">
    <div class="service-photo" role="img" aria-label="Photo of a team gathered around a laptop" style="background:linear-gradient(135deg,#6b5440,#c8a880 60%,#4b3a2c)"></div>
    <h3>Lorem Ipsum</h3>
    <p>Lorem ipsum dolor sit amet, consectetur adipiscing elit, sed do eiusmod tempor incididunt ut labore et dolore magna aliqua.</p>
    <a class="btn" href="#">READ MORE</a>
  </article>
  <article class="service-card featured" style="left:433px">
    <div class="service-photo" role="img" aria-label="Photo of a businesswoman holding a tablet" style="background:linear-gradient(135deg,#7c8a84,#c8d2cc 50%,#39404a)"></div>
    <h3>Lorem Ipsum</h3>
    <p>Lorem ipsum dolor sit amet, consectetur adipiscing elit, sed do eiusmod tempor incididunt ut labore et dolore magna aliqua.</p>
    <a class="btn" href="#">READ MORE</a>
  </article>
  <article class="service-card" style="left:755px">
    <div class="service-photo" role="img" aria-label="Photo of two colleagues working at a laptop" style="background:linear-gradient(135deg,#9aa8b4,#dfe4e8 55%,#2e3e5a)"></div>
    <h3>Lorem Ipsum</h3>
    <p>Lorem ipsum dolor sit amet, consectetur adipiscing elit, sed do eiusmod tempor incididunt ut labore et dolore magna aliqua.</p>
    <a class="btn" href="#">READ MORE</a>
  </article>
  <article class="service-card" style="left:1077px">
    <div class="service-photo" role="img" aria-label="Photo of workers in a warehouse" style="background:linear-gradient(135deg,#c79a3a,#8a9aa8 55%,#4b5560)"></div>
    <h3>Lorem Ipsum</h3>
    <p>Lorem ipsum dolor sit amet, consectetur adipiscing elit, sed do eiusmod tempor incididunt ut labore et dolore magna aliqua.</p>
    <a class="btn" href="#">READ MORE</a>
  </article>
</section>

<section class="about">
  <div class="about-mark"><span class="mark"></span><span class="name">LUMOSHIRE</span></div>
  <h2 class="section-title"><span class="accent">ABOUT</span> US</h2>
  <p>Lorem ipsum dolor sit amet, consectetur adipiscing elit, sed do eiusmod tempor incididunt ut labore et dolore magna aliqua. Quis ipsum suspendisse ultrices gravida. Risus commodo viverra maecenas accumsan lacus vel facilisis. Lorem ipsum dolor sit amet, consectetur adipiscing elit, sed do eiusmod tempor incididunt ut labore et dolore magna aliqua. Quis ipsum suspendisse ultrices gravida. Risus commodo viverra maecenas accumsan lacus vel facilisis.</p>
  <a class="btn" href="#">READ MORE</a>
</section>

<section class="mission">
  <div class="mission-photo" role="img" aria-label="Faint photo of people in a bright office with plants"></div>
  <h2>OUR MISSION</h2>
  <p class="p1">Lorem ipsum dolor sit amet, consectetur adipiscing elit, sed do eiusmod tempor incididunt ut labore et dolore magna aliqua. Quis ipsum suspendisse ultrices gravida. Risus commodo viverra maecenas accumsan lacus vel facilisis.</p>
  <p class="p2">Sed ut perspiciatis unde omnis iste natus error sit voluptatem accusantium doloremque laudantium, totam rem aperiam, eaque ipsa quae ab illo inventore veritatis et quasi architecto beatae vitae dicta sunt explicabo. Nemo enim ipsam voluptatem quia voluptas sit aspernatur aut odit aut fugit, sed quia consequuntur magni .</p>
  <a class="btn" href="#">View More...</a>
</section>

<section class="what">
  <h2 class="section-title"><span class="accent">WHAT WE</span> DO</h2>
  <p>Lorem ipsum dolor sit amet, consectetur adipiscing elit, sed do eiusmod tempor incididunt ut labore et dolore magna aliqua. Quis ipsum suspendisse ultrices gravida. Risus commodo viverra maecenas accumsan lacus vel facilisis. Lorem ipsum dolor sit amet, consectetur adipiscing elit, sed do eiusmod tempor incididunt ut labore et dolore magna aliqua.</p>
  <a class="btn" href="#">READ MORE</a>
  <div class="monitor" role="img" aria-label="Illustration of a desktop monitor showing the recruitment web app sign-in screen"></div>
</section>

<section class="news">
  <h2>NEWS AND EVENTS</h2>
  <article class="news-card tall" style="left:110px">
    <h3>Lorem ipsum dolor sit amet, consectetur adipiscing elit, sed do</h3>
    <p>Research shows that the initial coloni-sation of gut microbiota in piglets occurs at least within the immediate prenatal period.</p>
    <span class="learn">Learn More <svg width="22" height="14" viewBox="0 0 22 14"><circle cx="8" cy="7" r="6" fill="#ddd"/><path d="M6 7h12M14 3l4 4-4 4" fill="none" stroke="#222" stroke-width="1.6"/></svg></span>
  </article>
  <div class="news-photo" role="img" aria-label="Photo of a smiling woman holding a tablet in an office" style="background:linear-gradient(135deg,#8a8f96,#d8d2c8 50%,#2f3b52)"></div>
  <article class="news-card tall" style="left:444px">
    <h3>Lorem ipsum dolor sit amet, consectetur adipiscing elit, sed do</h3>
    <p>A drop in retail dairy prices in recent months has jeopardised milk process-ing plants and farmers in Poland and Lithuania,</p>
    <span class="learn">Learn More <svg width="22" height="14" viewBox="0 0 22 14"><circle cx="8" cy="7" r="6" fill="#ddd"/><path d="M6 7h12M14 3l4 4-4 4" fill="none" stroke="#222" stroke-width="1.6"/></svg></span>
  </article>
  <div class="news-photo" role="img" aria-label="Photo of a woman working at a laptop in a home office" style="left:462px;background:linear-gradient(135deg,#2f4a4a,#6b7a6a 50%,#c89a3a)"></div>
  <article class="news-card short" style="top:109px">
    <h3>Lorem ipsum dolor sit amet, consectetur adipiscing elit, sed do</h3>
    <p>Russia's Verna-9 crossbreed. Photo: Alex Morin New tests of the Russian Verna</p>
    <span class="learn">Learn More <svg width="22" height="14" viewBox="0 0 22 14"><circle cx="8" cy="7" r="6" fill="#ddd"/><path d="M6 7h12M14 3l4 4-4 4" fill="none" stroke="#222" stroke-width="1.6"/></svg></span>
  </article>
  <article class="news-card short" style="top:387px">
    <h3>Lorem ipsum dolor sit amet, consectetur adipiscing elit, sed do</h3>
    <p>Farmers hold a unique power to be an innovative part of the solutions to climate change.</p>
    <span class="learn">Learn More <svg width="22" height="14" viewBox="0 0 22 14"><circle cx="8" cy="7" r="6" fill="#ddd"/><path d="M6 7h12M14 3l4 4-4 4" fill="none" stroke="#222" stroke-width="1.6"/></svg></span>
  </article>
  <a class="btn" href="#">VIEW MORE</a>
</section>

<footer class="site-footer">
  <svg class="footer-rings" width="520" height="460" viewBox="0 0 520 460" aria-hidden="true">
    <g fill="none" stroke="#2a2a2a" stroke-width="2"><circle cx="260" cy="230" r="120"/><circle cx="260" cy="230" r="160"/><circle cx="260" cy="230" r="200"/><circle cx="260" cy="230" r="240"/></g>
  </svg>
  <div class="footer-brand"><span class="mark"></span><span class="name">LUMOSHIRE</span></div>
  <div class="contact">
    <h4>CONTACT US</h4>
    <ul class="contact-list">
      <li><svg width="12" height="16" viewBox="0 0 12 16"><path d="M6 0a6 6 0 0 0-6 6c0 4.5 6 10 6 10s6-5.5 6-10a6 6 0 0 0-6-6zm0 8.5A2.5 2.5 0 1 1 6 3.5a2.5 2.5 0 0 1 0 5z" fill="#fff"/></svg><span>4th Floor, Lumoshire<br>street, Ward 11, District 10,<br>Riverside City</span></li>
      <li><svg width="13" height="13" viewBox="0 0 24 24"><path d="M6.6 10.8a15 15 0 0 0 6.6 6.6l2.2-2.2c.3-.3.7-.4 1-.2 1.1.4 2.3.6 3.6.6.6 0 1 .4 1 1V20c0 .6-.4 1-1 1A17 17 0 0 1 3 4c0-.6.4-1 1-1h3.5c.6 0 1 .4 1 1 0 1.3.2 2.5.6 3.6.1.3 0 .7-.2 1z" fill="#fff"/></svg><span>+1 555 010 2040</span></li>
      <li><svg width="14" height="12" viewBox="0 0 14 12"><rect x="0" y="0" width="14" height="12" rx="1" fill="#fff"/><path d="M0 1l7 5 7-5" fill="none" stroke="#121212" stroke-width="1.4"/></svg><span>hello@lumoshire.com</span></li>
    </ul>
  </div>
  <div class="newsletter">
    <h4>SUBSCRIBE TO OUR NEWSLETTER</h4>
    <div class="subscribe">Enter Your Email<a class="btn" href="#">Subscribe</a></div>
  </div>
  <p class="legal left">© Copyrights 2024 Lumoshire &nbsp;|&nbsp; All Rights Reserved</p>
  <p class="legal right">Terms&amp;condtions | Privacy Policy | About Us | Support</p>
</footer>

</body>
</html>
```